R7M Meridian Business Card Design

We need a business card created for our New Business "R7M Meridian"<br/><br/>The business card design is up to you however the following information must be on the business card:<br/><br/>Front of the business card -<br/>Email :dorianv@r7mmeridian.nz<br/>Mobile: +64 (0) 22 4871 659<br/>Website: www.r7mmeridian.nz<br/>Card Owner Name: Dorian Valcourt<br/>Company Title: Business Development Manager<br/>Slogan: "The BEST of both worlds". <br/>Logo On the front attached to the design brief<br/><br/>On the back: <br/>Space on the back for 4 more versions of the logo across the bottom of the card indicating different subsidiary brands - R7M Coffee, R7M Arts, R7M ?? (The card will be used for all of these brands - We Will add the extra subsidiary logos to the design once the design is finished (We are a graphics design team). <br/><br/>Other than that we want a premium feeling logo that remains universally usable depending on the business entity that we are using the card for. The use of bright bold colours would be great but we still want the card to feel premium.
Target Market(s)
Gift Design and Manufacturing Companies
Contact Information for Business Card
Front of the business card -
Email :dorianv@r7mmeridian.nz
Mobile: +64 (0) 22 4871 659
Website: www.r7mmeridian.nz
Card Owner Name: Dorian Valcourt
Company Title: Business Development Manager
Slogan: "The BEST of both worlds".
Logo On the front attached to the design brief

```html
<!DOCTYPE html>
<html lang="en">
<head>
<meta charset="utf-8">
<title>R7M Meridian Business Card</title>
<link rel="stylesheet" href="https://fonts.googleapis.com/css2?family=Open+Sans:wght@400;600&family=Tinos:wght@700&display=swap">
<style>
  :root {
    --backdrop: #2f333a;
    --brand-blue: #3447a0;
    --card-black: #141414;
    --card-white: #ffffff;
    --ink-dark: #222222;
    --ink-grey: #555555;
  }
  * { box-sizing: border-box; margin: 0; padding: 0; }
  html, body {
    width: 1200px; height: 1000px; overflow: hidden;
    background: var(--backdrop);
    font-family: "Open Sans", sans-serif;
  }
  .stage {
    width: 1200px; height: 1000px;
    display: flex; flex-direction: column; align-items: center; justify-content: center;
    gap: 44px;
  }
  .card {
    position: relative;
    width: 760px; height: 430px;
    border-radius: 26px;
    overflow: hidden;
  }
  /* Company name set as plain wordmark text */
  .wordmark {
    color: var(--brand-blue);
    font-weight: 600;
    white-space: nowrap;
  }
  /* Back */
  .card-back { background: var(--card-black); }
  .wordmark-main {
    position: absolute; left: 0; right: 0; top: 128px;
    text-align: center;
    font-size: 54px; letter-spacing: 1px;
  }
  .sub-brands {
    position: absolute; left: 40px; right: 40px; bottom: 58px;
    display: flex; justify-content: space-around;
  }
  .wordmark-small { font-size: 17px; }
  /* Front */
  .card-front { background: var(--card-white); }
  .front-wordmark {
    position: absolute; left: 0; width: 345px; top: 166px;
    text-align: center;
    font-size: 32px;
  }
  .divider {
    position: absolute; left: 345px; top: 110px;
    width: 2px; height: 190px; background: var(--ink-dark);
  }
  .details { position: absolute; left: 372px; top: 118px; }
  .holder-name {
    font-family: "Tinos", serif; font-weight: 700;
    font-size: 27px; color: var(--brand-blue);
    text-transform: uppercase; letter-spacing: 1px;
  }
  .holder-title { font-size: 18px; color: var(--ink-grey); margin-bottom: 10px; }
  .contact-list { list-style: none; }
  .contact-list li {
    display: flex; align-items: center; gap: 10px;
    font-size: 18px; color: var(--ink-grey); line-height: 30px;
  }
  .contact-list svg { width: 15px; height: 15px; flex: none; }
  .slogan-band {
    position: absolute; left: 0; right: 0; top: 350px; height: 50px;
    background: var(--brand-blue);
    display: flex; align-items: center; justify-content: center;
    color: var(--card-white); font-size: 20px;
  }
</style>
</head>
<body>
<main class="stage">
  <section class="card card-back" aria-label="Card back">
    <div class="wordmark wordmark-main">R7M Meridian</div>
    <div class="sub-brands">
      <div class="wordmark wordmark-small">R7M Meridian</div>
      <div class="wordmark wordmark-small">R7M Meridian</div>
      <div class="wordmark wordmark-small">R7M Meridian</div>
      <div class="wordmark wordmark-small">R7M Meridian</div>
    </div>
  </section>

  <section class="card card-front" aria-label="Card front">
    <div class="wordmark front-wordmark">R7M Meridian</div>
    <div class="divider"></div>
    <div class="details">
      <h1 class="holder-name">Dorian Valcourt</h1>
      <p class="holder-title">Business Development Manager</p>
      <ul class="contact-list">
        <li>
          <svg viewBox="0 0 24 24" aria-hidden="true"><path fill="#3447a0" d="M6.6 10.8a15.1 15.1 0 0 0 6.6 6.6l2.2-2.2a1 1 0 0 1 1-.25 11.4 11.4 0 0 0 3.6.57 1 1 0 0 1 1 1V20a1 1 0 0 1-1 1A17 17 0 0 1 3 4a1 1 0 0 1 1-1h3.5a1 1 0 0 1 1 1c0 1.25.2 2.45.57 3.57a1 1 0 0 1-.25 1z"/></svg>
          +64 (0) 22 4871 659
        </li>
        <li>
          <svg viewBox="0 0 24 24" aria-hidden="true"><rect x="2" y="5" width="20" height="14" fill="#3447a0"/><path d="M2 5l10 8 10-8" fill="none" stroke="#fff" stroke-width="2"/></svg>
          dorianv@r7mmeridian.nz
        </li>
        <li>
          <svg viewBox="0 0 24 24" aria-hidden="true"><circle cx="12" cy="12" r="10" fill="none" stroke="#3447a0" stroke-width="2"/><ellipse cx="12" cy="12" rx="4.5" ry="10" fill="none" stroke="#3447a0" stroke-width="2"/><path d="M2 12h20M4 7h16M4 17h16" stroke="#3447a0" stroke-width="2"/></svg>
          www.r7mmeridian.nz
        </li>
      </ul>
    </div>
    <div class="slogan-band">The BEST of both worlds</div>
  </section>
</main>
</body>
</html>
```